Delvane Advisory Partners
Simple
Dr. Paul Merideth
347 Brookfield Lane
Los Altos, CA 94024
mtorvell@delvaneadvisorypartners.example
www.delvaneadvisorypartners.example
I wish to create a classy, simple, elegant single-sided business card for my consulting company.
I only wish for my number, e-mail, and website information to be on the card, NOT my address. Also, no need to put "cell" or "e-mail" or "web" on the card, just the information.

```html
<!DOCTYPE html>
<html lang="en">
<head>
<meta charset="utf-8">
<title>Delvane Advisory Partners — Business Card</title>
<link rel="stylesheet" href="https://fonts.googleapis.com/css2?family=Source+Sans+3:wght@400;700&family=Tinos&family=Cinzel:wght@500&display=swap">
<style>
  :root {
    --page-bg: #e9e6e1;
    --card-white: #ffffff;
    --card-black: #1c1c1c;
    --swoosh-light: #d6d6d6;
    --swoosh-dark: #7a7a7a;
    --ink: #1a1a1a;
    --ink-muted: #6e6e6e;
    --ink-inverse: #f4f4f4;
  }
  * { margin: 0; padding: 0; box-sizing: border-box; }
  html, body {
    width: 1200px;
    height: 780px;
    overflow: hidden;
    background: var(--page-bg);
  }
  .canvas {
    position: relative;
    width: 1200px;
    height: 780px;
    display: flex;
    align-items: center;
    justify-content: center;
  }
  .card {
    position: relative;
    width: 1050px;
    height: 600px;
    border-radius: 34px;
    overflow: hidden;
    background: var(--card-white);
    box-shadow: 0 10px 30px rgba(0,0,0,0.18);
  }
  .card__shapes {
    position: absolute;
    inset: 0;
    width: 100%;
    height: 100%;
  }
  .card__holder {
    position: absolute;
    top: 44px;
    right: 56px;
    text-align: right;
    font-family: "Source Sans 3", Arial, sans-serif;
  }
  .card__holder-name {
    font-weight: 700;
    font-size: 28px;
    color: var(--ink);
    line-height: 1.15;
  }
  .card__holder-company {
    font-weight: 400;
    font-size: 19px;
    color: var(--ink-muted);
    margin-top: 4px;
  }
  .card__brand {
    position: absolute;
    left: 60px;
    top: 210px;
    width: 520px;
    text-align: center;
    font-family: "Cinzel", "Times New Roman", serif;
    font-weight: 500;
    font-size: 44px;
    line-height: 1.2;
    letter-spacing: 2px;
    color: var(--ink);
  }
  .card__contact {
    position: absolute;
    right: 56px;
    bottom: 58px;
    text-align: right;
    font-family: "Tinos", "Times New Roman", serif;
    font-size: 22px;
    line-height: 1.5;
    color: var(--ink-inverse);
  }
  .card__contact-phone { margin-bottom: 30px; }
</style>
</head>
<body>
  <main class="canvas">
    <section class="card" aria-label="Business card for Delvane Advisory Partners">
      <svg class="card__shapes" viewBox="0 0 1050 600" preserveAspectRatio="none" aria-hidden="true">
        <defs>
          <linearGradient id="swooshGradient" x1="0" y1="1" x2="1" y2="0">
            <stop offset="0" stop-color="var(--swoosh-light)"/>
            <stop offset="0.6" stop-color="var(--swoosh-dark)"/>
            <stop offset="1" stop-color="var(--swoosh-light)"/>
          </linearGradient>
        </defs>
        <path class="card__swoosh" d="M 40 600 C 390 545, 760 390, 1050 75 L 1050 120 C 800 430, 430 560, 120 600 Z" fill="url(#swooshGradient)"/>
        <path class="card__dark-field" d="M 120 600 C 430 560, 800 430, 1050 120 L 1050 600 Z" fill="var(--card-black)"/>
      </svg>

      <div class="card__holder">
        <p class="card__holder-name">Dr. Paul Merideth</p>
        <p class="card__holder-company">Delvane Advisory Partners</p>
      </div>

      <p class="card__brand">Delvane Advisory Partners</p>

      <div class="card__contact">
        <p class="card__contact-phone">650-555-0142</p>
        <p class="card__contact-email">mtorvell@delvaneadvisorypartners.example</p>
        <p class="card__contact-web">www.delvaneadvisorypartners.example</p>
      </div>
    </section>
  </main>
</body>
</html>
```